Willowmere Loft B&B Business Card

This beautiful high-class B&B is looking for a business card that stands out from the rest. They are in the middle of the countryside, have chickens, geese and a dog. They also love bumble bees.

I was maybe thinking a rustic drawing / print of a bumble bee and a sketch of the house, I am not sure.. I quite like the feel of this... http://www.tarnwick-mill.co.uk/

Industry/Entity Type

Business

Contact Information for Business Card

Willowmere Loft
Bed & Breakfast
Brackleford, Hensworth, Somerset, TA14 7QP
01632 960418 | www.willowmereloft.co.uk

```html
<!DOCTYPE html>
<html lang="en">
<head>
<meta charset="utf-8">
<title>Willowmere Loft Bed &amp; Breakfast – Business Card</title>
<link rel="stylesheet" href="https://fonts.googleapis.com/css2?family=EB+Garamond:wght@500&family=Lato:wght@300&display=swap">
<style>
  :root {
    --backdrop: #bdbdbd;
    --card: #000000;
    --gold: #e4c873;
    --gold-deep: #b8923f;
    --gold-light: #f6e6a8;
  }
  * { margin: 0; padding: 0; box-sizing: border-box; }
  html, body {
    width: 1200px;
    height: 801px;
    overflow: hidden;
    background: var(--backdrop);
  }
  .business-card {
    position: absolute;
    left: 41px;
    top: 79px;
    width: 1118px;
    height: 643px;
    background: var(--card);
  }
  .house-artwork {
    position: absolute;
    left: 0;
    top: 96px;
    width: 672px;
    height: 323px;
    display: block;
  }
  .brand {
    position: absolute;
    left: 0;
    width: 616px;
    text-align: center;
    font-family: "EB Garamond", Georgia, serif;
    font-weight: 500;
    color: var(--gold);
  }
  .brand-name { top: 446px; font-size: 58px; line-height: 1; }
  .brand-tagline { top: 520px; font-size: 44px; line-height: 1; }
  .divider {
    position: absolute;
    left: 701px;
    top: 0;
    width: 3px;
    height: 100%;
    background: var(--gold);
  }
  .contact-line {
    position: absolute;
    left: 760px;
    font-family: "Lato", Helvetica, Arial, sans-serif;
    font-weight: 300;
    font-size: 28px;
    line-height: 1;
    color: var(--gold);
    white-space: nowrap;
  }
  .contact-address-1 { top: 174px; }
  .contact-address-2 { top: 260px; }
  .contact-phone { top: 344px; letter-spacing: 2.5px; }
  .contact-web { top: 418px; }
</style>
</head>
<body>
  <div class="business-card">
    <svg class="house-artwork" viewBox="0 0 672 323" role="img" aria-label="Gold line drawing of the farmhouse with pitched roofs, chimney and arched doorway">
      <defs>
        <linearGradient id="goldWash" x1="0" y1="0" x2="1" y2="1">
          <stop offset="0" stop-color="#3a2d12"/>
          <stop offset="0.5" stop-color="#5a4520"/>
          <stop offset="1" stop-color="#2a200c"/>
        </linearGradient>
      </defs>
      <polygon points="0,0 672,0 672,323 0,323" fill="url(#goldWash)" opacity="0.55"/>
    </svg>

    <div class="brand brand-name">Willowmere Loft</div>
    <div class="brand brand-tagline">Bed &amp; Breakfast</div>

    <div class="divider"></div>

    <p class="contact-line contact-address-1">Brackleford, Hensworth</p>
    <p class="contact-line contact-address-2">Somerset, TA14 7QP</p>
    <p class="contact-line contact-phone">01632 960418</p>
    <p class="contact-line contact-web">www.willowmereloft.co.uk</p>
  </div>
</body>
</html>
```